Fast Business Card Project

I need a business card with the name RENATO DUARTE stylized on one side and my email on the other (renatocosta4711@mailnova.com)

Industry/Entity Type

Business

Contact Information for Business Card

www.trilhamar.com.br

```html
<!DOCTYPE html>
<html lang="pt-BR">
<head>
<meta charset="utf-8">
<title>Cartão de visita — Renato Duarte</title>
<link rel="stylesheet" href="https://fonts.googleapis.com/css2?family=Arimo:wght@700&display=swap">
<style>
  :root {
    --card-black: #030303;
    --paper-white: #ffffff;
    --text-light: #e6e6e6;
    --glow: rgba(255, 255, 255, 0.55);
  }
  html, body {
    margin: 0;
    padding: 0;
    width: 1200px;
    height: 686px;
    overflow: hidden;
    background: var(--paper-white);
  }
  .card-back {
    position: relative;
    width: 1200px;
    height: 686px;
    background: var(--paper-white);
  }
  .card-face {
    position: absolute;
    left: 0;
    top: 0;
    width: 1200px;
    height: 580px;
    background: var(--card-black);
  }
  .edge-stripe {
    position: absolute;
    left: 0;
    top: 590px;
    width: 1200px;
    height: 9px;
    background: var(--card-black);
  }
  .contact-line {
    position: absolute;
    left: 87px;
    margin: 0;
    font-family: "Arimo", Arial, sans-serif;
    font-weight: 700;
    font-size: 23px;
    line-height: 28px;
    letter-spacing: 0.42em;
    color: var(--text-light);
    text-shadow: 0 0 6px var(--glow), 0 0 12px var(--glow);
    white-space: nowrap;
  }
  .contact-email { top: 77px; }
  .contact-divider { top: 163px; left: 97px; }
  .contact-web { top: 254px; }
  .holder-name {
    top: 470px;
    font-size: 30px;
    line-height: 36px;
    letter-spacing: 0.5em;
  }
</style>
</head>
<body>
  <div class="card-back">
    <div class="card-face">
      <p class="contact-line contact-email">renatocosta4711@mailnova.com</p>
      <p class="contact-line contact-divider">-</p>
      <p class="contact-line contact-web">www.trilhamar.com.br</p>
      <p class="contact-line holder-name">RENATO DUARTE</p>
    </div>
    <div class="edge-stripe"></div>
  </div>
</body>
</html>
```